Vemra. Packaging for mood-boosting energy drink mix. Upbeat and uplifting.

I need a mockup of a pouch package + a stick. I included an image of a Aqua Tarn pouch + stick for reference. I do not have a die line for the pouch, so feel free to just use the same relative dimensions for the pouch and create a rendering. Here are the specifications for the packaging that I need:
1. The logo is included in the uploaded files. Please use the one that says "bright day spark" beneath "vemra." The logo should take up about the top 1/3 to 1/2 of the pouch.
2. The pouch should be mostly white, especially behind the logo, but feel free to explore yellow or orange for the bottom 1/2 to 2/3 of the packaging.
3. In the center of the packaging, below the logo, please have the product name appear, "mood-boosting energy drink mix" similar to where "Fluid Amplifier" is placed.
4. Below that, create an image of a glass with a stick pouring into it like in the Aqua Tarn pouch.
5. Below the glass, in the bottom center of the package, include "16 sticks. Net Wt. 4 oz. (114 g)
6. On the left side, please include callouts, from top to bottom, "energy blend (80mg caffeine, taurine) + happy blend (saffron, st. john's wort, rhodiola).
7. On the right side, please include callouts, from top to bottom, "electrolytes + vitamins + 0g sugar"
8. Somewhere else on the front of the packaging, please include the flavor name "golden berry," perhaps where they do on the aqua tarn pouch.
9. For the stick, use your creativity.
10. There is no back of packaging to design for this project.

Target Market(s)

My target consumer leads a very active lifestyle and cares deeply about health & wellness.

Colors
0094D4
00A9DD
6FCCEA
C7EBF8
E9F6FB
FFC000
F8CF3A
FAE287
FDF2CF
FEFAEE
F0912C
F2A743
F7CA91
FBE8D2
FDF5EE
EE7325
F08F49
F5BC92
FAE3D3
FDF4ED

Requirements
Must have
• My packaging must make people feel good and maybe even smile when they see it. A brand that does this well is Penn. (www.pennvita-example.com)
Nice to have
• I like 60's Mod Design if you need some inspiration. The packaging should also convey a sense of levity. Like you'll float or dance through life after drinking this.

```html
<!DOCTYPE html>
<html lang="en">
<head>
<meta charset="utf-8">
<title>Vemra – Mood-Boosting Energy Drink Mix Packaging</title>
<link rel="stylesheet" href="https://fonts.googleapis.com/css2?family=Fredoka:wght@500;600&family=Montserrat:wght@600;700&family=Roboto:wght@400&display=swap">
<style>
  :root {
    --blue-deep: #0094D4;
    --blue: #1589C8;
    --blue-sky: #6FCCEA;
    --yellow: #FFC000;
    --yellow-soft: #F8CF3A;
    --orange: #EE7325;
    --orange-mid: #F08F49;
    --orange-light: #F2A743;
    --peach: #F7CA91;
    --white: #FFFFFF;
    --pouch-white: #F4F5F6;
    --seal-grey: #E4E6E8;
    --frame-grey: #C9CDD2;
    --ink-white: #FFFFFF;
  }
  * { box-sizing: border-box; margin: 0; padding: 0; }
  html, body { width: 1200px; height: 1200px; overflow: hidden; }
  body { background: var(--white); position: relative; font-family: "Roboto", Arial, sans-serif; }

  /* Pouch */
  .pouch {
    position: absolute; left: 115px; top: 215px; width: 765px; height: 850px;
    background: var(--pouch-white); border-radius: 18px 18px 10px 10px;
    overflow: hidden;
  }
  .pouch__seal { position: absolute; left: 0; right: 0; top: 0; height: 30px; background: var(--seal-grey); }
  .pouch__zip { position: absolute; left: 40px; right: 40px; top: 98px; height: 8px; border-top: 2px solid var(--seal-grey); border-bottom: 2px solid var(--seal-grey); }

  .brand { position: absolute; left: 0; right: 0; top: 135px; text-align: center; }
  .brand__name {
    font-family: "Fredoka", sans-serif; font-weight: 600; font-size: 150px; line-height: 1;
    color: var(--orange); letter-spacing: -2px;
  }
  .brand__tagline {
    position: absolute; left: 430px; top: 150px;
    font-family: "Fredoka", sans-serif; font-weight: 600; font-size: 24px; color: var(--orange);
  }

  .panel { position: absolute; left: 88px; top: 315px; width: 590px; height: 535px; }
  .panel__pattern {
    position: absolute; inset: 0;
    background: linear-gradient(135deg, var(--orange) 0%, var(--yellow-soft) 35%, var(--orange-mid) 60%, var(--blue-sky) 85%, var(--orange-light) 100%);
  }
  .panel__label {
    position: absolute; left: 125px; top: 130px; width: 345px; height: 235px;
    background: var(--blue); border: 8px solid var(--frame-grey); text-align: center; color: var(--ink-white);
  }
  .product-name__line1 { font-family: "Montserrat", sans-serif; font-weight: 700; font-size: 26px; margin-top: 14px; }
  .product-name__line2 { font-family: "Montserrat", sans-serif; font-weight: 600; font-size: 21px; margin-top: 2px; }
  .prep-icon { display: block; margin: 8px auto 0; }
  .callouts { font-size: 7.5px; line-height: 2.2; margin-top: 16px; }

  .panel__band {
    position: absolute; left: 0; right: 0; bottom: 0; height: 50px; background: var(--orange);
    display: flex; align-items: center; padding-left: 12px; gap: 40px;
  }
  .flavor { font-family: "Fredoka", sans-serif; font-weight: 600; font-size: 17px; color: var(--yellow); }
  .net-weight { font-family: "Montserrat", sans-serif; font-size: 15px; color: var(--ink-white); }
  .net-weight strong { font-weight: 700; font-size: 18px; }

  /* Stick */
  .stick { position: absolute; left: 900px; top: 352px; width: 172px; height: 712px; background: var(--pouch-white); overflow: hidden; }
  .stick__seal { position: absolute; left: 0; right: 0; top: 0; height: 24px; background: var(--seal-grey); }
  .stick__brand {
    position: absolute; left: 86px; top: 185px; transform: translate(-50%, -50%) rotate(90deg);
    white-space: nowrap; text-align: center;
  }
  .stick__name { font-family: "Fredoka", sans-serif; font-weight: 600; font-size: 82px; line-height: 1; color: var(--orange); }
  .stick__tagline { font-family: "Fredoka", sans-serif; font-weight: 600; font-size: 13px; color: var(--orange); }
  .stick__label {
    position: absolute; left: 15px; right: 10px; top: 300px; height: 46px; background: var(--blue);
    color: var(--ink-white); text-align: center; font-family: "Montserrat", sans-serif; padding-top: 8px;
  }
  .stick__label-line1 { font-weight: 700; font-size: 13px; }
  .stick__label-line2 { font-weight: 600; font-size: 11px; }
  .stick__pattern {
    position: absolute; left: 15px; right: 10px; top: 346px; height: 287px;
    background: linear-gradient(160deg, var(--blue-deep) 0%, var(--peach) 35%, var(--orange-light) 60%, var(--blue-sky) 78%, var(--orange) 100%);
  }
  .stick__band {
    position: absolute; left: 15px; right: 10px; top: 633px; bottom: 0; background: var(--orange);
    text-align: center; padding-top: 12px;
  }
  .stick__band .flavor { font-size: 18px; }
</style>
</head>
<body>
  <section class="pouch">
    <div class="pouch__seal"></div>
    <div class="pouch__zip"></div>
    <div class="brand">
      <div class="brand__name">vemra</div>
      <div class="brand__tagline">bright day spark</div>
    </div>
    <div class="panel">
      <div class="panel__pattern" role="img" aria-label="Mod geometric pattern of circles, quarter rounds and rings in orange, yellow and blue"></div>
      <div class="panel__label">
        <div class="product-name__line1">MOOD - BOOSTING</div>
        <div class="product-name__line2">ENERGY DRINK MIX</div>
        <svg class="prep-icon" width="170" height="80" viewBox="0 0 170 80" fill="none" stroke="#E9F6FB" stroke-width="1.5">
          <g transform="rotate(28 22 10)"><rect x="2" y="5" width="44" height="8"/></g>
          <path d="M36 50 h26 l-3 30 h-20 z"/>
          <path d="M37 58 h24 l-2 22 h-20 z" fill="#6FCCEA" stroke="none" opacity="0.7"/>
          <g fill="#6FCCEA">
            <path d="M95 55 q-11 14 0 24 q11-10 0-24z"/>
            <path d="M122 55 q-11 14 0 24 q11-10 0-24z"/>
            <path d="M149 55 q-11 14 0 24 q11-10 0-24z"/>
          </g>
        </svg>
        <div class="callouts">
          energy blend (80mg caffeine, taurine) + happy blend (saffron, st. john's wort, rhodiola)<br>
          electrolytes + vitamins + 0g sugar
        </div>
      </div>
      <div class="panel__band">
        <span class="flavor">Golden berry</span>
        <span class="net-weight"><strong>16 sticks.</strong> Net Wt. 4 oz. (114 g)</span>
      </div>
    </div>
  </section>

  <section class="stick">
    <div class="stick__seal"></div>
    <div class="stick__brand">
      <div class="stick__name">vemra</div>
      <div class="stick__tagline">bright day spark</div>
    </div>
    <div class="stick__label">
      <div class="stick__label-line1">MOOD-BOOSTING</div>
      <div class="stick__label-line2">ENERGY DRINK MIX</div>
    </div>
    <div class="stick__pattern" role="img" aria-label="Mod geometric pattern of rings and quarter rounds in blue, yellow and orange"></div>
    <div class="stick__band"><span class="flavor">Golden berry</span></div>
  </section>
</body>
</html>
```